Revamp Of Landing Page For an Automated AI Voice Agents Agency

here is my current landing page https://app.brightfunnelstudio.example/v2/preview/KXWQPmR4hLsDnTfYvJcA?notrack=true

Please use all my current content and imagery of ai agents in your new design. Make it easy to ready, easy to navigate and easy to understand

I am looking for a SLEEK shiny polished looking website. I like Dark themed sites but am open to see light themed sites too so please dont be shy.

The site should have an Ai Voice Agent Theme about it. Maybe look and feel of futureistic but simple and not intimidating to the average person...

Here are a couple website designs I like for reference:
https://q4t.example/
https://ai-bots.mervinholt.example/
https://chatvexo.example/ai-agents

Target Market(s)

b2b

Industry/Entity Type

AI Voice Agents

Coding

Coded - Design and coding required

Font styles to use
Other font styles liked:
• open

Requirements
Must have
• all elements and content and images used in existing design.
Nice to have
• open
Should not have
• open

```html
<!DOCTYPE html>
<html lang="en">
<head>
<meta charset="utf-8">
<title>VoxWorks – AI Voice Agents</title>
<link href="https://fonts.googleapis.com/css2?family=Fira+Sans:wght@400;500;600;700&display=swap" rel="stylesheet">
<style>
:root{
  --purple:#6a3fe0;
  --purple-soft:#8a5cf0;
  --violet-deep:#1a0b4a;
  --ink:#111118;
  --muted:#4a4a5a;
  --navy:#0e1522;
  --white:#ffffff;
  --lav:#f1ecfc;
  --line:#e4e1ee;
}
*{box-sizing:border-box;margin:0;padding:0}
html,body{width:1200px;height:5259px;overflow:hidden}
body{font-family:"Fira Sans",Arial,sans-serif;color:var(--ink);background:var(--white);position:relative}
.abs{position:absolute}
.accent{color:var(--purple)}
.btn{display:inline-block;background:var(--purple);color:var(--white);font-weight:500;border-radius:4px;text-align:center}
.logo{font-weight:600;letter-spacing:2px;display:flex;align-items:center;gap:10px}
.logo .dot{width:14px;height:14px;border-radius:50%;border:2px solid var(--purple-soft)}

/* nav */
.nav{top:0;left:0;width:1200px;height:70px;background:var(--white)}
.nav .logo{left:75px;top:20px;font-size:26px;color:var(--ink)}
.nav .menu{left:443px;top:25px;display:flex;gap:22px;font-size:15px;color:var(--ink)}
.nav .login{left:1008px;top:15px;width:117px;height:40px;line-height:40px;font-size:16px}

/* hero */
.hero{top:70px;left:0;width:1200px;height:481px;background:linear-gradient(100deg,#1b0a47 0%,#2a0f68 55%,#3a1590 100%)}
.hero .tag{left:75px;top:116px;padding:6px 22px;background:rgba(255,255,255,.08);color:#e8e2ff;font-size:15px;letter-spacing:.5px}
.hero h1{left:75px;top:160px;width:680px;color:var(--white);font-size:28px;font-weight:600;line-height:39px}
.hero .rating{left:75px;top:252px;color:#e5def7;font-size:13px}
.hero .rating b{color:#ffb400}
.hero .signup{left:75px;top:287px;display:flex}
.hero .signup span{width:313px;height:39px;line-height:39px;padding-left:10px;background:#25124f;border:1px solid #3e2a78;color:#8c82aa;font-size:12px}
.hero .signup .btn{width:230px;height:39px;line-height:39px;border-radius:0 3px 3px 0;font-size:16px}
.hero .dots{left:75px;top:358px;display:flex;gap:8px}
.hero .dots i{width:32px;height:4px;background:#fff;border-radius:2px}
.hero .dots i:first-child{background:var(--purple-soft)}
.hero .art{left:755px;top:52px;width:290px;height:348px;border-radius:40px;background:radial-gradient(circle at 50% 45%,#b7a3ff 0%,#6d48d8 45%,rgba(58,21,144,0) 75%)}

/* workforce */
.sec-title{width:1200px;text-align:center;font-size:56px;font-weight:600;line-height:60px}
.feature-card{left:75px;width:1050px;border-radius:30px;overflow:hidden}
.card-sales{top:802px;height:429px;background:linear-gradient(110deg,#faf8ff 0%,#efe8fd 100%);border:1px solid var(--line)}
.card-recep{top:1284px;height:427px;background:#000}
.feature-card h3{position:absolute;font-size:28px;font-weight:500;color:var(--purple)}
.feature-card p{position:absolute;font-size:14px;line-height:21px}
.ticks{position:absolute;display:grid;grid-template-columns:270px 260px;row-gap:32px;font-size:15px;font-weight:600}
.ticks li{list-style:none;display:flex;align-items:center;gap:10px}
.ticks svg{width:18px;height:18px}
.feature-card .btn{position:absolute;width:152px;height:39px;line-height:39px;font-size:16px;border-radius:3px}
.card-recep h3{color:#8a6bff}
.card-recep p,.card-recep .ticks{color:var(--white)}

.phone{position:absolute;width:232px;height:420px;background:#fff;border:6px solid #111;border-radius:22px;overflow:hidden;font-size:8px}
.phone .status{display:flex;justify-content:space-between;padding:6px 12px 2px;font-weight:600}
.phone .head{display:flex;align-items:center;gap:6px;padding:6px 10px;border-bottom:1px solid #eee;font-weight:600}
.phone .head i{width:16px;height:16px;border-radius:50%;background:var(--purple)}
.bubble{margin:10px 8px;padding:7px 9px;max-width:150px;line-height:12px;border-radius:3px}
.bubble.me{background:var(--purple);color:#fff;margin-left:auto}
.bubble.them{background:#f0f0f3;color:#222}

/* use case tiles */
.tile{top:1765px;width:327px;height:429px;border-radius:6px;overflow:hidden;background:linear-gradient(180deg,#47506a 0%,#2b3146 55%,#14161f 100%)}
.tile .go{position:absolute;right:18px;top:16px;width:36px;height:36px;border-radius:50%;background:#fff;display:flex;align-items:center;justify-content:center}
.tile h4{position:absolute;left:13px;top:327px;color:#fff;font-size:22px;font-weight:500}
.tile p{position:absolute;left:13px;top:364px;width:300px;color:#e8e8ee;font-size:13px;line-height:19px}

/* wish band */
.band{left:0;width:1200px;color:#fff;text-align:center;background:linear-gradient(100deg,#150838 0%,#2b1074 50%,#170a3f 100%)}
.wish{top:2276px;height:326px}
.wish h2{position:absolute;top:60px;width:1200px;font-size:54px;font-weight:600}
.wish h2 span{color:#9d7aff}
.wish .sub{position:absolute;top:126px;width:1200px;font-size:22px}
.wish p{position:absolute;top:168px;left:190px;width:820px;font-size:14px;line-height:21px}
.band .btn{position:absolute;height:39px;line-height:39px;font-size:16px}

/* employee */
.mini{top:2772px;width:332px;height:126px;background:#f7f6fb;border:1px solid var(--line);border-radius:8px;padding:18px 26px}
.mini .t{display:flex;align-items:center;gap:14px;font-size:22px;font-weight:500}
.mini .t i{width:36px;height:36px;border-radius:8px;background:var(--purple);display:block}
.mini p{margin-top:14px;font-size:15px;line-height:21px;color:#222}

/* faq */
.faq-h{left:75px;top:2980px;font-size:56px;font-weight:600}
.faq-sub{left:75px;top:3055px;font-size:22px}
.acc{left:75px;width:615px;background:#fff;border:1px solid var(--line);border-radius:4px;padding:0 18px;font-size:16px;font-weight:500}
.acc .q{display:flex;justify-content:space-between;align-items:center;height:55px}
.acc p{font-size:14px;font-weight:400;line-height:20px;color:#333;width:520px}
.faq-art{left:735px;top:3000px;width:428px;height:368px;border-radius:50%;background:radial-gradient(circle,#e7dcff 0%,#c9b1ff 40%,rgba(255,255,255,0) 72%)}

/* hire */
.hire{position:absolute;top:3482px;left:0;width:1200px;height:759px;color:#fff;background:linear-gradient(160deg,#5a2bd6 0%,#2c0f80 45%,#120632 100%);overflow:hidden}
.hire h2{position:absolute;left:84px;top:70px;font-size:56px;font-weight:600;line-height:59px}
.hire .lead{position:absolute;left:84px;top:210px;width:600px;font-size:22px;line-height:31px}
.hire .btn{position:absolute;left:84px;top:284px;width:254px;height:37px;line-height:37px;font-size:16px}
.hire h3{position:absolute;left:75px;top:387px;font-size:40px;font-weight:600}
.hire .promise{position:absolute;left:75px;top:440px;width:460px;font-size:22px;line-height:31px}
.hire .item{position:absolute;left:75px;display:flex;align-items:center;gap:22px;font-size:22px}
.hire .art{position:absolute;left:775px;top:100px;width:330px;height:580px;border-radius:30px;background:radial-gradient(ellipse at 50% 50%,#9be9ff 0%,#6b5cff 30%,rgba(42,16,128,0) 70%)}

/* voices */
.voices h2{position:absolute;top:4320px;width:1200px;text-align:center;font-size:44px;font-weight:500}
.voices .sub{position:absolute;top:4390px;left:240px;width:720px;text-align:center;font-size:22px;line-height:31px}
.pill{top:4470px;width:262px;height:51px;background:#5a2bd6;border-radius:4px;display:flex;align-items:center;padding:0 14px;gap:12px;color:#fff;font-size:15px}
.pill i{width:34px;height:34px;border-radius:50%;background:#f0eaff;display:block}
.pill b{margin-left:auto;color:#ffd23f;font-size:14px;letter-spacing:1px}
.vdots{left:543px;top:4551px;display:flex;gap:8px}
.vdots i{width:32px;height:4px;background:#d7d3e2}
.vdots i:first-child{background:var(--purple)}

/* cta */
.cta{top:4645px;height:311px}
.cta h2{position:absolute;top:68px;width:1200px;font-size:36px;font-weight:600;line-height:41px}
.cta p{position:absolute;top:168px;left:160px;width:880px;font-size:14px;line-height:21px}

/* footer */
.foot{position:absolute;top:4956px;left:0;width:1200px;height:303px;background:var(--navy);color:#fff}
.foot .logo{position:absolute;left:75px;top:58px;font-size:26px}
.foot .disc{position:absolute;left:75px;top:106px;width:280px;font-size:13px;line-height:20px;color:#d9dce4}
.col{position:absolute;top:46px;font-size:14px}
.col h5{font-size:17px;font-weight:500;margin-bottom:14px}
.col li{list-style:none;margin-bottom:14px;color:#dfe2ea}
.col li::before{content:"•";color:var(--purple-soft);margin-right:8px}
.contact li::before{content:none}
.contact li{display:flex;gap:12px;align-items:flex-start;line-height:19px;margin-bottom:16px}
.contact svg{width:22px;height:22px;flex:none}
.foot .bar{position:absolute;left:0;top:262px;width:1200px;height:41px;border-top:1px solid #253044;display:flex;justify-content:space-between;align-items:center;padding:0 75px;font-size:11px;color:#cfd3dd}
</style>
</head>
<body>

<header class="nav abs">
  <div class="logo abs"><span class="dot"></span>VOXWORKS</div>
  <nav class="menu abs"><span>Product ▾</span><span>Use Cases ▾</span><span>Pricing</span><span>Book a Demo</span></nav>
  <a class="btn login abs">Login</a>
</header>

<section class="hero abs">
  <div class="tag abs">// AI VOICE AGENTS</div>
  <h1 class="abs">That Answer Calls, Book Appts, Send Emails, Text Messages, Follow Up Reminders,</h1>
  <div class="rating abs"><b>★</b> 4.9 - Excellent Rating Software Trusted By Users</div>
  <div class="signup abs"><span>Enter you email</span><a class="btn">Get 14 Days Free Trial</a></div>
  <div class="dots abs"><i></i><i></i><i></i></div>
  <div class="art abs" role="img" aria-label="Friendly robot voice agent surrounded by floating chat bubbles"></div>
</section>

<h2 class="sec-title abs" style="top:633px">Meet Your New<br><span class="accent">AI-Powered Workforce</span></h2>

<section class="feature-card card-sales abs">
  <h3 style="left:75px;top:78px">Ai Sales Agent</h3>
  <p style="left:75px;top:124px;width:545px">Brian will take your inbound sales calls. Will give all detailed information to the customer, answer questions in a normal conversational tone and can book sales appointments or transfer hot prospects to a human to close the sale.</p>
  <ul class="ticks" style="left:75px;top:212px">
    <li><svg viewBox="0 0 20 20"><circle cx="10" cy="10" r="8" fill="none" stroke="#6a3fe0" stroke-width="1.8"/><path d="M6 10l3 3 5-6" fill="none" stroke="#6a3fe0" stroke-width="1.8"/></svg>24/7 Intelligent Sales Rep</li>
    <li><svg viewBox="0 0 20 20"><circle cx="10" cy="10" r="8" fill="none" stroke="#6a3fe0" stroke-width="1.8"/><path d="M6 10l3 3 5-6" fill="none" stroke="#6a3fe0" stroke-width="1.8"/></svg>Instant Response, Zero Wait</li>
    <li><svg viewBox="0 0 20 20"><circle cx="10" cy="10" r="8" fill="none" stroke="#6a3fe0" stroke-width="1.8"/><path d="M6 10l3 3 5-6" fill="none" stroke="#6a3fe0" stroke-width="1.8"/></svg>Boosts Conversion Rates</li>
    <li><svg viewBox="0 0 20 20"><circle cx="10" cy="10" r="8" fill="none" stroke="#6a3fe0" stroke-width="1.8"/><path d="M6 10l3 3 5-6" fill="none" stroke="#6a3fe0" stroke-width="1.8"/></svg>Follow-Up Automation</li>
  </ul>
  <a class="btn" style="left:75px;top:310px">Read More</a>
  <div class="phone" style="left:741px;top:38px">
    <div class="status"><span>12:30 am</span><span>▪▪ ◔</span></div>
    <div class="head"><i></i>Ai Sales Agent</div>
    <div class="bubble me">Hi there! I'm Alan, your sales agent!</div>
    <div class="bubble them">I'm interested in your product.</div>
    <div class="bubble me">Awesome! I can help with that. What product are you looking at?</div>
    <div class="bubble them">The Pro Max Package.</div>
    <div class="bubble me">Great choice! It includes: Feature A, Feature B. $99/month. Would you like a free trial?</div>
  </div>
</section>

<section class="feature-card card-recep abs">
  <div class="phone" style="left:76px;top:46px">
    <div class="status"><span>12:30 am</span><span>▪▪ ◔</span></div>
    <div class="head"><i></i>Ai Receptionist</div>
    <div class="bubble me">Welcome Center. Hello! I'm Grace, your virtual assistant</div>
    <div class="bubble them">Hi, I have a question about hours.</div>
    <div class="bubble me">Sure! We're open Mon–Fri from 9 AM to 6 PM. Would you like to book a visit?</div>
    <div class="bubble them">Yes, tomorrow at 11.</div>
    <div class="bubble me">Got it! You're booked. You'll receive a confirmation</div>
  </div>
  <h3 style="left:425px;top:78px">Ai Receptionist</h3>
  <p style="left:431px;top:122px;width:545px">Cody handles all your calls 24/7. You can also set him to only take overflow calls and after hours. He can send eails and sms messages and even book appointments over the call.</p>
  <ul class="ticks" style="left:431px;top:210px;grid-template-columns:355px 260px">
    <li><svg viewBox="0 0 20 20"><circle cx="10" cy="10" r="8" fill="none" stroke="#8a6bff" stroke-width="1.8"/><path d="M6 10l3 3 5-6" fill="none" stroke="#8a6bff" stroke-width="1.8"/></svg>24/7 &amp; Transfer To Appropriate Dept.</li>
    <li><svg viewBox="0 0 20 20"><circle cx="10" cy="10" r="8" fill="none" stroke="#8a6bff" stroke-width="1.8"/><path d="M6 10l3 3 5-6" fill="none" stroke="#8a6bff" stroke-width="1.8"/></svg>Appointment Scheduling</li>
    <li><svg viewBox="0 0 20 20"><circle cx="10" cy="10" r="8" fill="none" stroke="#8a6bff" stroke-width="1.8"/><path d="M6 10l3 3 5-6" fill="none" stroke="#8a6bff" stroke-width="1.8"/></svg>Answering FAQs</li>
    <li><svg viewBox="0 0 20 20"><circle cx="10" cy="10" r="8" fill="none" stroke="#8a6bff" stroke-width="1.8"/><path d="M6 10l3 3 5-6" fill="none" stroke="#8a6bff" stroke-width="1.8"/></svg>Multichannel Support</li>
  </ul>
  <a class="btn" style="left:431px;top:308px">Read More</a>
</section>

<article class="tile abs" style="left:75px" role="img" aria-label="Photo of a humanoid AI agent wearing a headset">
  <span class="go"><svg width="14" height="14" viewBox="0 0 14 14"><path d="M3 11L11 3M5 3h6v6" fill="none" stroke="#111" stroke-width="1.5"/></svg></span>
  <h4>Ai Appointment Setter</h4><p>Book Appts &amp; Reservations On Auto Pilot</p>
</article>
<article class="tile abs" style="left:437px" role="img" aria-label="Photo of an AI agent with headset working at a desk">
  <span class="go"><svg width="14" height="14" viewBox="0 0 14 14"><path d="M3 11L11 3M5 3h6v6" fill="none" stroke="#111" stroke-width="1.5"/></svg></span>
  <h4>Ai Lead Qualifier</h4><p>Conversate With Prospects To Qualify Before Handing Over To Sales Team</p>
</article>
<article class="tile abs" style="left:798px" role="img" aria-label="Photo of a humanoid AI assistant in a bright office">
  <span class="go"><svg width="14" height="14" viewBox="0 0 14 14"><path d="M3 11L11 3M5 3h6v6" fill="none" stroke="#111" stroke-width="1.5"/></svg></span>
  <h4>Ai Follow Up Reminders</h4><p>Calls, Sends SMS &amp; Email Reminders</p>
</article>

<section class="band wish abs">
  <h2>Your Wish Is <span>Their Command</span></h2>
  <div class="sub">Your New Ai Agents Will Never Call In Sick And Will Never Complain!</div>
  <p>With your new team of AI Agents, handling inbound calls, sending emails and sms messages, booking appointments and handling customer service inquiries is going to save you a ton of time and money.</p>
  <a class="btn" style="left:453px;top:230px;width:290px">Get An Instant Free Demo</a>
</section>

<h2 class="sec-title abs" style="top:2685px">An Employee That <span class="accent">Never Gets Sick!</span></h2>
<div class="mini abs" style="left:75px"><div class="t"><i></i>Trained In Seconds</div><p>Learns Your Entire Website In Seconds</p></div>
<div class="mini abs" style="left:434px"><div class="t"><i></i>Worldwide</div><p>Works Anywhere In The Globe</p></div>
<div class="mini abs" style="left:793px"><div class="t"><i></i>User-friendly</div><p>Your Ai Agents Sound As If They're Real Humans</p></div>

<h2 class="faq-h abs">Do You <span class="accent">Have Questions?</span></h2>
<div class="faq-sub abs">Let our AI assistant guide you with quick, clear answers.</div>
<div class="acc abs" style="top:3102px;height:149px">
  <div class="q">What exactly are the AI Voice Agents? <span>⌃</span></div>
  <p>AI Voice Agents are specialized human sounding bots, having smart and masterful conversations and each is expertly trained in seconds for a specific business function.</p>
</div>
<div class="acc abs" style="top:3272px"><div class="q">How will these AI Voice Agents benefit <span>⌄</span></div></div>
<div class="acc abs" style="top:3347px"><div class="q">Are they easy to use? <span>⌄</span></div></div>
<div class="faq-art abs" role="img" aria-label="Illustration of a robot assistant above a phone with chat bubbles"></div>

<section class="hire">
  <h2>Our Ai Agents<br>Our Ready To Be Hired</h2>
  <div class="lead">Lightning-Fast Responses, Instant answers, no coffee, bathroom or lunch breaks needed</div>
  <a class="btn">Get An Instant Free Demo</a>
  <h3>Our Promise To You</h3>
  <div class="promise">Reliable, responsive, and built to support your growth.</div>
  <div class="item" style="top:540px"><svg width="64" height="64" viewBox="0 0 64 64"><path d="M32 6l20 8v16c0 14-9 23-20 28C21 53 12 44 12 30V14z" fill="none" stroke="#fff" stroke-width="2.5"/><path d="M22 32l7 7 13-15" fill="none" stroke="#fff" stroke-width="2.5"/></svg>14-day money-back guarantee</div>
  <div class="item" style="top:634px"><svg width="64" height="64" viewBox="0 0 64 64"><circle cx="32" cy="32" r="24" fill="none" stroke="#fff" stroke-width="2.5"/><text x="32" y="38" text-anchor="middle" font-size="16" fill="#fff" font-family="Fira Sans,Arial,sans-serif">24</text></svg>24/7 Customer Support</div>
  <div class="art" role="img" aria-label="Glowing neon lightning bolt"></div>
</section>

<section class="voices">
  <h2>Customer Voices, <span class="accent">Real Results</span></h2>
  <div class="sub">After Our Customers Have A Conversation With Their New Ai Voice Agent They Give Us 5 Stars!</div>
</section>
<div class="pill abs" style="left:-217px"><i></i>Liam<b>★★★★★</b></div>
<div class="pill abs" style="left:75px"><i></i>Sarah<b>★★★★★</b></div>
<div class="pill abs" style="left:371px"><i></i>Jordan<b>★★★★★</b></div>
<div class="pill abs" style="left:669px"><i></i>Anita<b>★★★★★</b></div>
<div class="pill abs" style="left:965px"><i></i>Emily<b>★★★★★</b></div>
<div class="vdots abs"><i></i><i></i><i></i></div>

<section class="band cta abs">
  <h2>These AI Agents Can Help Your Business Tremendously.<br>Imagine The Possibilities</h2>
  <p>We Will Create An Ai Agent Customized For Your Business At No Cost. Simply Click The Button Above And Your Very Own Ai Agent Will Be Calling You In Just A Couple Minutes. Experience The Magic And Get Ready To Be Very Impressed!</p>
  <a class="btn" style="left:456px;top:223px;width:290px">Get An Instant Free Demo</a>
</section>

<footer class="foot">
  <div class="logo"><span class="dot"></span>VOXWORKS</div>
  <p class="disc">This site is not a part of the SocialHub website or SocialHub Inc. Additionally, this site is NOT endorsed by SocialHub in any way.</p>
  <ul class="col" style="left:441px"><h5>Quick Links</h5><li>Product</li><li>Use Cases</li><li>Pricing</li><li>Book a Demo</li><li>Testimonials</li></ul>
  <ul class="col" style="left:647px"><h5>Products</h5><li>Ai Sales Agent</li><li>Ai Receptionist</li><li>Ai Lead Qualifier</li><li>Ai Appointment Setter</li><li>Ai Follow Up Reminders</li></ul>
  <ul class="col contact" style="left:910px"><h5>Contact Us</h5>
    <li><svg viewBox="0 0 24 24"><circle cx="12" cy="12" r="11" fill="#6a3fe0"/><path d="M8 7l2 0 1 3-1.5 1a6 6 0 003 3l1-1.5 3 1v2c-5 0-9-4-9-9z" fill="#fff"/></svg>555-014-2290</li>
    <li><svg viewBox="0 0 24 24"><circle cx="12" cy="12" r="11" fill="#6a3fe0"/><path d="M12 6a4 4 0 014 4c0 3-4 8-4 8s-4-5-4-8a4 4 0 014-4z" fill="#fff"/></svg>48 Harbor Row<br>Leeds, UK LS1 4DY</li>
    <li><svg viewBox="0 0 24 24"><circle cx="12" cy="12" r="11" fill="#6a3fe0"/><rect x="6.5" y="8" width="11" height="8" fill="none" stroke="#fff" stroke-width="1.4"/><path d="M6.5 8l5.5 4.5L17.5 8" fill="none" stroke="#fff" stroke-width="1.4"/></svg>contact@voxworks.example</li>
  </ul>
  <div class="bar"><span>Earnings &amp; Products Disclaimer &nbsp;|&nbsp; Privacy Policy &nbsp;|&nbsp; Term &amp; Conditions</span><span>© 2025 VoxWorks</span></div>
</footer>

</body>
</html>
```